Geschäftspapiere für unternehmerische Holding für Beteiligungen, Projektgesellschaften und kaufmännische Steuerung
Zielgruppe
Die Wolsten GmbH ist eine unternehmerische Holding für Beteiligungen, Projektgesellschaften und kaufmännische Steuerung. Sie übernimmt Management-, Controlling- und Strukturierungsaufgaben für verbundene Unternehmen.
Zielgruppe sind Banken, Investoren, Geschäftspartner, Steuerberater, Rechtsanwälte, Behörden sowie Geschäftsführungen und Gesellschafter von Beteiligungs- und Projektgesellschaften.
Aufgabenstellung
Gesucht wird ein digitales Briefpapier für die Wolsten GmbH, das sowohl als PDF/Dokumentvorlage als auch beim Ausdruck professionell funktioniert.
Wichtig ist ein sehr klarer, hochwertiger und seriöser Auftritt. Das Design soll reduziert, strukturiert und geschäftlich wirken – keine verspielten Elemente, keine überladenen Grafiken, keine auffälligen Muster.
Das Briefpapier muss drucktauglich sein. Bitte ausreichende Druckränder und Sicherheitsabstände berücksichtigen, damit Kopf- und Fußbereich auch auf normalen Büro- und Laserdruckern sauber ausgegeben werden können. Das Layout soll sowohl digital als auch gedruckt stimmig aussehen.
Format: DIN A4 Hochformat.
Gewünschte Inhalte:
* Logo der Wolsten GmbH
* Firmenname: Wolsten GmbH
* Geschäftsanschrift: Lindauer Weg 58, 80339 München
* Telefon: 089 52809163
* E-Mail: info@wolstenhq.example
* Webseite: wolstenhq.example
* Geschäftsführung: Dipl.-Wirtschaftsing. (FH) Bernd Ostholt
* Registergericht / Amtsgericht München HRB 720458
* Bankverbindung IBAN DE619082 4415 0007 8126 30
Besonderer Wert liegt auf:
* hochwertiger Holding-/Investment-Anmutung
* sehr guter Lesbarkeit
* klarer Kopf- und Fußzeile
* sauberer Typografie
* professioneller Nutzbarkeit für Angebote, Verträge, Behörden- und Bankkorrespondenz
Bitte das Design so anlegen, dass es später als editierbare Word-/PDF-Vorlage genutzt werden kann und sowohl das Logo, als auch die Farben entsprechend verwenden.

```html
<!DOCTYPE html>
<html lang="de">
<head>
<meta charset="utf-8">
<title>Wolsten GmbH – Briefpapier</title>
<link href="https://fonts.googleapis.com/css2?family=Carlito:wght@400;700&display=swap" rel="stylesheet">
<style>
  :root {
    --navy: #1c3a5c;
    --slate: #2e3a48;
    --mist: #d5dade;
    --cloud: #e9ecef;
    --grey-dark: #4a4a4a;
    --grey-light: #b9bcbf;
    --ink: #1e1e1e;
    --stage: #eeeeee;
    --paper: #ffffff;
  }
  * { margin: 0; padding: 0; box-sizing: border-box; }
  html, body { width: 1200px; height: 640px; overflow: hidden; }
  body {
    background: radial-gradient(ellipse at 50% 40%, #f6f6f6 0%, var(--stage) 70%, #e6e6e6 100%);
    font-family: "Carlito", "Calibri", sans-serif;
    color: var(--ink);
    position: relative;
  }
  .sheet {
    position: absolute;
    top: 34.5px;
    width: 365px;
    height: 515px;
    background: var(--paper);
    box-shadow: 0 2px 10px rgba(0,0,0,0.14);
    overflow: hidden;
  }
  .sheet--left { left: 34.5px; }
  .sheet--center { left: 418px; }
  .sheet--right { left: 800px; }

  .brand {
    position: absolute;
    top: 28px;
    width: 97px;
    height: 35px;
    display: flex;
    align-items: center;
    justify-content: center;
    gap: 6px;
  }
  .sheet--left .brand { left: 31.5px; }
  .sheet--center .brand { left: 134px; }
  .sheet--right .brand { left: 237px; }
  .brand__square { width: 8px; height: 8px; background: var(--navy); }
  .brand__name {
    font-size: 17px;
    font-weight: 400;
    letter-spacing: 1.5px;
    color: var(--navy);
    text-transform: uppercase;
  }

  .rule {
    position: absolute;
    left: 16px;
    width: 337px;
    height: 1.5px;
    display: flex;
  }
  .rule--head { top: 73.5px; }
  .rule--foot { top: 409.5px; background: var(--navy); }
  .rule span { display: block; height: 100%; }
  .seg-navy { background: var(--navy); }
  .seg-grey { background: var(--grey-dark); }
  .seg-light { background: var(--grey-light); }

  .contact {
    position: absolute;
    top: 423px;
    left: 34.5px;
    font-size: 8.4px;
    line-height: 12px;
  }
  .contact__col { position: absolute; top: 0; white-space: nowrap; }
  .contact__col--address { left: 0; }
  .contact__col--reach { left: 93px; }
  .contact__col--lead { left: 196.5px; }
  .contact__col--lead strong { font-weight: 700; }
  .divider {
    position: absolute;
    width: 0.8px;
    background: var(--ink);
  }
  .divider--reach { left: 118px; top: 424px; height: 33px; }
  .divider--lead { left: 222px; top: 424px; height: 33px; }
  .divider--bank { left: 207px; top: 468px; height: 16px; }

  .legal {
    position: absolute;
    top: 472px;
    font-size: 6.2px;
    white-space: nowrap;
  }
  .legal strong { font-weight: 700; }
  .legal--register { left: 34.5px; }
  .legal--bank { left: 215px; }

  .band {
    position: absolute;
    left: 0;
    bottom: 0;
    width: 100%;
    height: 4.5px;
    display: flex;
  }
  .band span { display: block; height: 100%; }

  .palette {
    position: absolute;
    left: 34.5px;
    top: 575px;
    display: flex;
  }
  .palette__swatch { width: 30.75px; height: 30px; }
  .palette__swatch--navy { background: var(--navy); }
  .palette__swatch--slate { background: var(--slate); }
  .palette__swatch--mist { background: var(--mist); }
  .palette__swatch--cloud { background: var(--cloud); border: 0.75px solid #cfd3d6; }
</style>
</head>
<body>

  <!-- Variante 1 -->
  <section class="sheet sheet--left">
    <div class="brand"><span class="brand__square"></span><span class="brand__name">Wolsten</span></div>
    <div class="rule rule--head"><span class="seg-navy" style="width:169px"></span><span class="seg-grey" style="flex:1"></span></div>
    <div class="rule rule--foot"></div>
    <div class="contact">
      <div class="contact__col contact__col--address">Lindauer Weg 58<br>80339 München</div>
      <div class="contact__col contact__col--reach">T +49 89 52809163<br>E info@wolstenhq.example<br>W wolstenhq.example</div>
      <div class="contact__col contact__col--lead"><strong>Geschäftsführer:</strong><br>Dipl.-Wirtschaftsing. (FH)<br>Bernd Ostholt</div>
    </div>
    <span class="divider divider--reach"></span>
    <span class="divider divider--lead"></span>
    <p class="legal legal--register"><strong>Registergericht:</strong> Amtsgericht München HRB 720458</p>
    <span class="divider divider--bank"></span>
    <p class="legal legal--bank"><strong>IBAN</strong> DE61 9082 4415 0007 8126 30</p>
    <div class="band"><span class="seg-navy" style="width:183px"></span><span class="seg-grey" style="flex:1"></span></div>
  </section>

  <!-- Variante 2 -->
  <section class="sheet sheet--center">
    <div class="brand"><span class="brand__square"></span><span class="brand__name">Wolsten</span></div>
    <div class="rule rule--head"><span class="seg-light" style="width:84px"></span><span class="seg-navy" style="width:168px"></span><span class="seg-light" style="flex:1"></span></div>
    <div class="rule rule--foot"></div>
    <div class="contact">
      <div class="contact__col contact__col--address">Lindauer Weg 58<br>80339 München</div>
      <div class="contact__col contact__col--reach">T +49 89 52809163<br>E info@wolstenhq.example<br>W wolstenhq.example</div>
      <div class="contact__col contact__col--lead"><strong>Geschäftsführer:</strong><br>Dipl.-Wirtschaftsing. (FH)<br>Bernd Ostholt</div>
    </div>
    <span class="divider divider--reach"></span>
    <span class="divider divider--lead"></span>
    <p class="legal legal--register"><strong>Registergericht:</strong> Amtsgericht München HRB 720458</p>
    <span class="divider divider--bank"></span>
    <p class="legal legal--bank"><strong>IBAN</strong> DE61 9082 4415 0007 8126 30</p>
    <div class="band"><span class="seg-light" style="width:91px"></span><span class="seg-navy" style="width:183px"></span><span class="seg-light" style="flex:1"></span></div>
  </section>

  <!-- Variante 3 -->
  <section class="sheet sheet--right">
    <div class="brand"><span class="brand__square"></span><span class="brand__name">Wolsten</span></div>
    <div class="rule rule--head"><span class="seg-navy" style="width:169px"></span><span class="seg-grey" style="flex:1"></span></div>
    <div class="rule rule--foot"></div>
    <div class="contact">
      <div class="contact__col contact__col--address">Lindauer Weg 58<br>80339 München</div>
      <div class="contact__col contact__col--reach">T +49 89 52809163<br>E info@wolstenhq.example<br>W wolstenhq.example</div>
      <div class="contact__col contact__col--lead"><strong>Geschäftsführer:</strong><br>Dipl.-Wirtschaftsing. (FH)<br>Bernd Ostholt</div>
    </div>
    <span class="divider divider--reach"></span>
    <span class="divider divider--lead"></span>
    <p class="legal legal--register"><strong>Registergericht:</strong> Amtsgericht München HRB 720458</p>
    <span class="divider divider--bank"></span>
    <p class="legal legal--bank"><strong>IBAN</strong> DE61 9082 4415 0007 8126 30</p>
  </section>

  <div class="palette">
    <span class="palette__swatch palette__swatch--navy"></span>
    <span class="palette__swatch palette__swatch--slate"></span>
    <span class="palette__swatch palette__swatch--mist"></span>
    <span class="palette__swatch palette__swatch--cloud"></span>
  </div>

</body>
</html>
```